Glofarvik - Start-up company selling electricity

Hello let me tell you about Glofarvik.

Glofarvik is start-up company selling electricity in Iceland. The operations of the company consist of making power usage forecasts for our customers, purchasing the electricity wholesale from the energy producers, and selling the electricity to the consumer. We are focused on tech by using optimization and machine learning to minimize electricity prices to our customers. Our marketing strategy is to portray a tech company mindset and to show dedication to driving down the electricity price on the market.

We need your help to make our website pop. Possible concepts to work with are as follows:

- Iceland the land of ice and fire
- Green energy
- Innovation
- Tech and data science

Link to our website: https://prufa.glofarvik-example.is/
We are open to ideas.
Thank you!

Target Market(s)

Electricity consumers both homes and companies.

Number of Pages Required

1 page

Font styles to use
Serif
Sans Serif

```html
<!DOCTYPE html>
<html lang="en">
<head>
<meta charset="utf-8">
<title>Glofarvik – Same Electricity, Just Cheaper</title>
<link href="https://fonts.googleapis.com/css2?family=Fira+Sans:wght@400;500;600;700&family=Lato:wght@400;700&display=swap" rel="stylesheet">
<style>
  :root {
    --navy: #173a63;
    --red: #a82b22;
    --ink: #1f3350;
    --card: #f1f4f8;
    --footer: #f2f5f8;
    --white: #ffffff;
  }
  * { box-sizing: border-box; margin: 0; padding: 0; }
  html, body { width: 1200px; height: 2208px; overflow: hidden; }
  body { position: relative; background: var(--white); font-family: "Lato", sans-serif; color: var(--ink); }
  .abs { position: absolute; }
  .center { left: 0; width: 1200px; text-align: center; }
  .btn {
    position: absolute; display: flex; align-items: center; justify-content: center;
    border-radius: 18px; font-family: "Fira Sans", sans-serif; font-weight: 600; font-size: 12px;
    color: var(--white); background: var(--navy); text-decoration: none;
  }
  .btn--red { background: var(--red); }
  .btn--light { background: var(--white); color: var(--navy); font-weight: 500; }

  .site-header { top: 0; left: 0; width: 1200px; height: 80px; background: var(--white); }
  .brand { left: 88px; top: 26px; display: flex; align-items: center; gap: 10px;
    font-family: "Fira Sans", sans-serif; font-weight: 700; font-size: 28px; color: var(--navy); letter-spacing: .5px; }
  .brand__dot { width: 22px; height: 22px; border-radius: 50%; background: var(--red); }
  .nav { top: 32px; font-family: "Fira Sans", sans-serif; font-size: 13px; color: var(--ink); }
  .nav a { position: absolute; white-space: nowrap; color: inherit; text-decoration: none; }

  .hero { top: 80px; left: 0; width: 1200px; height: 604px;
    background: linear-gradient(180deg, #4b5058 0%, #6e7278 35%, #8b8a86 60%, #bdbcb9 85%, #d4d3d0 100%); }
  .hero__kicker { top: 276px; font-family: "Fira Sans", sans-serif; font-size: 27px; color: var(--white); font-weight: 400; }
  .hero__kicker b { font-weight: 600; }
  .hero__title { top: 318px; font-family: "Fira Sans", sans-serif; font-size: 50px; font-weight: 600; color: var(--white); }

  .section-title { font-family: "Fira Sans", sans-serif; font-weight: 600; color: var(--navy); }
  .section-text { font-size: 13px; line-height: 19px; color: var(--ink); }
  .card { top: 852px; width: 232px; height: 191px; background: var(--card); border-radius: 3px; text-align: center; }
  .card--raised { background: var(--white); box-shadow: 0 6px 24px rgba(23,58,99,.12); }
  .card__icon { position: absolute; left: 84px; top: 37px; width: 64px; height: 64px; border-radius: 50%;
    background: radial-gradient(circle at 35% 35%, #2a4f7c 0%, #173a63 60%, #7a2f35 100%); }
  .card__title { position: absolute; left: 0; width: 100%; top: 121px; font-family: "Fira Sans", sans-serif; font-weight: 500; font-size: 19px; color: var(--navy); }
  .card__sub { position: absolute; left: 0; width: 100%; top: 145px; font-size: 12px; color: var(--ink); }

  .band { top: 1196px; left: 0; width: 1200px; height: 199px;
    background: linear-gradient(120deg, #21436c 0%, #1b3d66 40%, #264a74 70%, #1c3f68 100%); }
  .band__title { top: 1232px; font-family: "Fira Sans", sans-serif; font-weight: 500; font-size: 39px; color: var(--white); letter-spacing: .5px; }
  .band__text { top: 1280px; font-family: "Fira Sans", sans-serif; font-size: 17px; color: var(--white); letter-spacing: .3px; }

  .price { top: 1620px; width: 200px; text-align: center; }
  .price__value { font-family: "Fira Sans", sans-serif; font-weight: 600; font-size: 39px; color: var(--red); line-height: 44px; }
  .price__unit { font-family: "Fira Sans", sans-serif; font-size: 15px; color: var(--navy); line-height: 19px; margin-top: 2px; }
  .divider { left: 600px; top: 1594px; width: 1px; height: 146px; background: #dfe4ea; }

  .site-footer { top: 1883px; left: 0; width: 1200px; height: 325px; background: var(--footer); }
  .footer-mark { left: 88px; top: 1955px; width: 52px; height: 52px; border-radius: 50%; background: var(--navy); }
  .footer-head { font-family: "Fira Sans", sans-serif; font-weight: 500; font-size: 17px; color: var(--navy); letter-spacing: .3px; }
  .footer-text { font-family: "Fira Sans", sans-serif; font-size: 12.5px; color: var(--ink); line-height: 19px; letter-spacing: .2px; }
  .call { left: 159px; top: 1998px; font-family: "Fira Sans", sans-serif; font-size: 19px; color: var(--red); display: flex; align-items: center; gap: 8px; }
  .call b { font-weight: 500; }
  .social { top: 2024px; width: 34px; height: 34px; border-radius: 50%; border: 1.5px solid var(--red); }
  .social--active { background: var(--red); }
  .to-top { left: 1064px; top: 1966px; width: 32px; height: 32px; border-radius: 50%; background: var(--red); }
</style>
</head>
<body>

<header class="abs site-header">
  <div class="abs brand"><span class="brand__dot"></span>Glofarvik</div>
  <nav class="abs nav" style="left:0;width:1200px">
    <a style="left:556px">About Glofarvik</a>
    <a style="left:692px">Terms of Business</a>
    <a style="left:832px">Question &amp; Answer</a>
  </nav>
  <a class="btn" style="left:985px;top:24px;width:127px;height:32px">Contact Us</a>
</header>

<section class="abs hero" role="img" aria-label="Photo of geodesic dome wellhead huts at a geothermal field under a cloudy winter sky"></section>
<svg class="abs" width="1200" height="700" viewBox="0 0 1200 700" style="top:0;left:0" aria-hidden="true">
  <polygon points="0,565 590,645 590,603 1200,684 1200,700 0,700" fill="#ffffff"/>
  <polyline points="0,565 590,641 590,603 1200,684" fill="none" stroke="#a82b22" stroke-width="7"/>
</svg>
<div class="abs center hero__kicker">WELCOME TO <b>GLOFARVIK</b></div>
<h1 class="abs center hero__title">Same Electricity ~ Just Cheaper!</h1>
<a class="btn btn--red" style="left:484px;top:410px;width:111px;height:30px">Company</a>
<a class="btn" style="left:604px;top:410px;width:111px;height:30px">Home</a>

<h2 class="abs center section-title" style="top:716px;font-size:40px">The future is exciting</h2>
<p class="abs center section-text" style="top:779px">Let's make the electricity system smarter together. Glofarvik uses artificial intelligence, data science<br>and automation to minimize costs and promote eccentricity</p>

<div class="abs card" style="left:88px">
  <div class="card__icon" role="img" aria-label="Icon of ice and fire"></div>
  <div class="card__title">Iceland</div>
  <div class="card__sub">the land of ice and fire</div>
</div>
<div class="abs card card--raised" style="left:352px">
  <div class="card__icon" role="img" aria-label="Icon of green energy"></div>
  <div class="card__title">Green energy</div>
</div>
<div class="abs card" style="left:616px">
  <div class="card__icon" role="img" aria-label="Icon of innovation"></div>
  <div class="card__title">Innovation</div>
</div>
<div class="abs card" style="left:880px">
  <div class="card__icon" role="img" aria-label="Icon of tech and data science"></div>
  <div class="card__title">Tech &amp; data science</div>
</div>

<a class="btn" style="left:544px;top:1084px;width:111px;height:31px">About Us</a>

<section class="abs band" role="img" aria-label="Deep blue faceted low-poly background"></section>
<h2 class="abs center band__title">Ranked #1 in customer satisfaction</h2>
<p class="abs center band__text">There are many variations of passages of lorem Ipsum available, but the majority have suffered</p>
<a class="btn btn--light" style="left:536px;top:1321px;width:143px;height:30px">Contact Us Today!</a>

<h2 class="abs center section-title" style="top:1468px;font-size:38px">Price list</h2>
<p class="abs center section-text" style="top:1529px">There are many variations of passages of Lorem Ipsum available, but the majority have<br>suffered alteration in some form, by injected humour,</p>
<div class="abs divider"></div>
<div class="abs price" style="left:368px">
  <div class="price__value">6.95</div>
  <div class="price__unit">ISK / kWh</div>
</div>
<div class="abs price" style="left:632px">
  <div class="price__value">6.22</div>
  <div class="price__unit">ISK / kWh electricity<br>acceleration</div>
</div>
<a class="btn" style="left:504px;top:1770px;width:191px;height:32px">Make a Price Comparison</a>

<footer class="abs site-footer"></footer>
<div class="abs footer-mark"></div>
<div class="abs footer-head" style="left:159px;top:1959px">Glofarvik</div>
<div class="abs call">Call Today!
  <svg width="16" height="16" viewBox="0 0 24 24" aria-hidden="true"><path d="M6.6 10.8a15.1 15.1 0 0 0 6.6 6.6l2.2-2.2a1 1 0 0 1 1-.25 11.4 11.4 0 0 0 3.6.57 1 1 0 0 1 1 1V20a1 1 0 0 1-1 1A17 17 0 0 1 3 4a1 1 0 0 1 1-1h3.5a1 1 0 0 1 1 1c0 1.25.2 2.450.57 3.6a1 1 0 0 1-.25 1z" fill="#a82b22"/></svg>
  <b>400-1234</b></div>
<div class="abs footer-text" style="left:159px;top:2020px">e. hallo@glofarvik-example.is</div>
<div class="abs footer-text" style="left:159px;top:2059px">Location:<br>Hafnarstígur 4, 170 Seltjarnarnes</div>

<div class="abs footer-head" style="left:511px;top:1959px">Quick Links</div>
<div class="abs footer-text" style="left:511px;top:1991px">About Glofarvik<br>Terms of Business<br>Question &amp; Answer</div>
<div class="abs footer-head" style="left:511px;top:2069px">Glofarvik ehf</div>
<div class="abs footer-text" style="left:511px;top:2097px">ID number: 510101-0000<br>VAT number: 100200</div>

<div class="abs footer-head" style="left:766px;top:1959px">© 2021 Glofarvik</div>
<div class="abs footer-text" style="left:766px;top:1987px;font-size:11px">All Rights Reserved.</div>
<span class="abs social" style="left:767px"></span>
<span class="abs social social--active" style="left:809px"></span>
<span class="abs social" style="left:850px"></span>
<span class="abs social" style="left:892px"></span>

<div class="abs to-top">
  <svg width="32" height="32" viewBox="0 0 32 32" aria-hidden="true"><polygon points="9,19 16,12 23,19" fill="#fff"/></svg>
</div>

</body>
</html>
```